IT CEO and Real Estate Investor

It should include two roles and be a two sided card (both roles can be one a single side with a creative view or on different sides).
Card must be creative and interesting, but still professional.
Phone countries(USA/Russia) might be as flags or words, whatever works better.
Boris Melnovetz
Skype: boris_m
E-mail: melnovetz@quorbamail.com
Facebook: plavbook.example/melnovetz
Linkedin: trelnet.example/in/melnovetz
Phone (US): 1(555)316-2947
Phone (RUS): 7(955)482-3170
First role:
Pex Lattor (pexlattor.example) - include logo or part of logo (the $)
E-Commerce Automation Solutions
Founder/CEO/CTO
Second role:
Real Estate Investor
Cleveland, OH
UPDATE:
Let's do one side as logo only and all information on the other side - I don't like designs with information on both sides.
I also really liked designs on black (or other dark) background

```html
<!DOCTYPE html>
<html lang="en">
<head>
<meta charset="utf-8">
<title>Pex Lattor — Business Card</title>
<link href="https://fonts.googleapis.com/css2?family=Montserrat:wght@400;500;600;700&display=swap" rel="stylesheet">
<style>
  :root {
    --brand-blue: #27a9e1;
    --ink-black: #050505;
    --paper-white: #ffffff;
    --canvas-bg: #e9ebee;
    --text-dark: #1a1a1a;
  }
  * { box-sizing: border-box; margin: 0; padding: 0; }
  html, body {
    width: 1200px; height: 900px; overflow: hidden;
    background: var(--canvas-bg);
    font-family: "Montserrat", Arial, sans-serif;
  }
  .card {
    position: absolute;
    width: 640px; height: 366px;
    border-radius: 22px;
    overflow: hidden;
    box-shadow: 0 8px 24px rgba(0,0,0,0.18);
  }

  /* Logo side */
  .card-front {
    left: 90px; top: 50px;
    background: var(--brand-blue);
    color: var(--paper-white);
  }
  .front-brand {
    position: absolute; left: 0; right: 0; top: 112px;
    display: flex; align-items: center; justify-content: center; gap: 22px;
  }
  .brand-dot {
    width: 74px; height: 74px; border-radius: 50%;
    background: var(--paper-white);
  }
  .front-name {
    font-size: 56px; font-weight: 600; letter-spacing: 4px;
  }
  .front-details {
    position: absolute; left: 0; right: 0; top: 222px;
    text-align: center; font-size: 15px; line-height: 24px; font-weight: 400;
  }
  .front-details .site-name { font-weight: 700; }
  .front-tagline {
    position: absolute; left: 0; right: 0; top: 292px;
    text-align: center; font-size: 17px; letter-spacing: 2px; font-weight: 500;
  }

  /* Information side */
  .card-back {
    left: 470px; top: 480px;
    background: var(--paper-white);
  }
  .back-dark-band {
    position: absolute; left: 0; right: 0; bottom: 0; height: 132px;
    background: var(--ink-black);
  }
  .back-dark-panel {
    position: absolute; right: 0; top: 128px; bottom: 0; width: 150px;
    background: var(--ink-black);
  }
  .back-mark {
    position: absolute; right: 28px; top: 160px;
    width: 96px; height: 96px; border-radius: 50%;
    background: var(--brand-blue);
  }
  .back-wordmark {
    position: absolute; left: 26px; top: 26px;
    font-size: 76px; font-weight: 600; letter-spacing: 2px;
    color: var(--brand-blue); line-height: 1;
  }
  .holder {
    position: absolute; left: 30px; top: 132px;
  }
  .holder-name {
    font-size: 22px; font-weight: 700; letter-spacing: 1px;
    color: var(--brand-blue); text-transform: uppercase;
  }
  .holder-role {
    font-size: 17px; font-weight: 500; color: var(--text-dark); line-height: 22px;
  }
  .contacts {
    position: absolute; left: 30px; top: 244px;
    list-style: none; color: var(--paper-white);
    font-size: 15px; line-height: 19px; font-weight: 500;
  }
  .contacts li { display: flex; align-items: center; gap: 12px; }
  .contact-icon { width: 12px; height: 12px; flex: none; }
  .contact-icon circle, .contact-icon path { fill: var(--brand-blue); }
  .contact-icon .stroke { fill: none; stroke: var(--brand-blue); stroke-width: 1.6; }
</style>
</head>
<body>

<section class="card card-front" aria-label="Card front">
  <div class="front-brand">
    <span class="brand-dot"></span>
    <span class="front-name">PEX LATTOR</span>
  </div>
  <p class="front-details">Cleveland, OH<br>www.<span class="site-name">pexlattor</span>.example</p>
  <p class="front-tagline">COMMERCE AUTOMATION SOLUTIONS</p>
</section>

<section class="card card-back" aria-label="Card back">
  <div class="back-dark-band"></div>
  <div class="back-dark-panel"></div>
  <div class="back-mark"></div>
  <div class="back-wordmark">PEX LATTOR</div>
  <div class="holder">
    <p class="holder-name">Boris Melnovetz</p>
    <p class="holder-role">Founder/CEO/CTO</p>
    <p class="holder-role">Real Estate Investor</p>
  </div>
  <ul class="contacts">
    <li><svg class="contact-icon" viewBox="0 0 12 12"><circle cx="6" cy="6" r="5"/></svg>boris_m</li>
    <li><svg class="contact-icon" viewBox="0 0 12 12"><path d="M2.5 1h2l1 3-1.4 1a6 6 0 0 0 2.4 2.4l1-1.4 3 1v2c0 .8-.7 1.5-1.5 1.5A9 9 0 0 1 1 2.5C1 1.7 1.7 1 2.5 1z"/></svg>(US): 1(555)316-2947</li>
    <li><svg class="contact-icon" viewBox="0 0 12 12"><path d="M2.5 1h2l1 3-1.4 1a6 6 0 0 0 2.4 2.4l1-1.4 3 1v2c0 .8-.7 1.5-1.5 1.5A9 9 0 0 1 1 2.5C1 1.7 1.7 1 2.5 1z"/></svg>(RUS): 7(955)482-3170</li>
    <li><svg class="contact-icon" viewBox="0 0 12 12"><rect class="stroke" x="1" y="2.5" width="10" height="7"/><path class="stroke" d="M1 2.5l5 4 5-4"/></svg>melnovetz@quorbamail.com</li>
    <li><svg class="contact-icon" viewBox="0 0 12 12"><circle cx="6" cy="6" r="5"/></svg>plavbook.example/melnovetz</li>
    <li><svg class="contact-icon" viewBox="0 0 12 12"><circle cx="6" cy="6" r="5"/></svg>trelnet.example/in/melnovetz</li>
  </ul>
</section>

</body>
</html>
```